Brookfern Clinical Trials Redesign

Website name: http://brookfernclinicaltrials.example/live/
Industry: medical & pharmaceutical
Target audience:
Clinical research patients
clinical research sponsors
clinical research referring doctors
Style/theme of your website design:
We want to customize the orbitel theme, emulating our competitors website
http://templatemarket.example/item/orbitel-responsive-multipurpose-wordpress-theme/4417203
Webdesign Examples?
http://www.tmxclinical.example/currently-enrolling-clinical-trials/
https://www.copperwellresearch.example/
What do you like about these sites:
These sites address all the needs of a clinical trial facility. The patient, the doctor and the sponsor. Also they have forms and sign up information for each trial they offer. The site needs to have SCHEMA markup and rich snippets. We have reviews and testimonial that need schema markup also, local NAP information and all the other rich snippet markups available.
How many pages need design:
8-12
List any colors:
existing color of website and logo
Target Market(s)
Target audience:
Industry/Entity Type
Pharmaceutical
Number of Pages Required
5+ page
Look and feel

```html
<!DOCTYPE html>
<html lang="en">
<head>
<meta charset="utf-8">
<title>Brookfern Clinical Trials</title>
<link rel="stylesheet" href="https://fonts.googleapis.com/css2?family=Ubuntu:wght@400;500&family=Arimo:wght@400;700&display=swap">
<style>
:root{
  --orange:#f07a0c;
  --green:#7cc21a;
  --blue:#0f72ab;
  --teal:#3aa6b5;
  --ink:#1a1a1a;
  --body:#555;
  --muted-bg:#eeeeee;
  --card-line:#cfcfcf;
  --white:#fff;
}
*{margin:0;padding:0;box-sizing:border-box}
html,body{width:864px;height:1200px;overflow:hidden;background:var(--white)}
body{position:relative;font-family:"Ubuntu",sans-serif;color:var(--body)}
h1,h2,h3{font-weight:400}
.abs{position:absolute}

.top-rule{left:0;top:0;width:864px;height:3px;display:flex}
.top-rule span{height:3px}
.site-header{left:0;top:0;width:864px;height:54px;background:var(--white)}
.brand{left:95px;top:10px;display:flex;align-items:center;gap:8px}
.brand-mark{width:30px;height:30px;background:var(--teal);border-radius:50%}
.brand-name{font-family:"Ubuntu",sans-serif;font-size:14px;line-height:15px;color:var(--teal);width:110px}
.main-nav{top:22px;left:0;font-family:"Arimo",sans-serif;font-size:10.5px;color:var(--ink)}
.main-nav a{position:absolute;white-space:nowrap;color:inherit;text-decoration:none}
.main-nav .active{color:var(--green)}
.search{left:754px;top:22px}

.hero{left:0;top:54px;width:864px;height:324px;background:linear-gradient(100deg,#d4d4d4 0%,#bdbdbd 35%,#9e9e9e 60%,#c9c9c9 100%)}
.hero-arrow{width:34px;height:34px;border-radius:50%;background:rgba(255,255,255,.25);display:flex;align-items:center;justify-content:center;top:186px}
.hero-dots{left:392px;top:362px;display:flex;gap:3px}
.hero-dots span{width:9px;height:9px;border-radius:50%;background:#ddd}
.hero-dots span:first-child{background:#fff}

.center{left:0;width:864px;text-align:center}
.welcome-title{top:397px;font-family:"Arimo",sans-serif;font-size:15px;color:var(--ink)}
.lead{font-size:10.6px;line-height:18px;color:var(--body)}
.welcome-text{top:424px;padding:0 92px}
.section-title{font-family:"Ubuntu",sans-serif;font-size:20px;color:var(--ink);letter-spacing:.6px}
.software-title{top:472px}
.software-text{top:505px;padding:0 100px}

.product-card{top:555px;width:327px;height:134px;border:1px solid var(--card-line);background:var(--white)}
.product-photo{position:absolute;left:-1px;top:-1px;width:126px;height:134px}
.product-body{position:absolute;left:125px;top:0;right:0;bottom:0;padding:10px 12px 0 12px}
.product-title{font-size:16px;line-height:20px;color:var(--ink);letter-spacing:.8px;white-space:nowrap;margin-bottom:6px}
.product-text{font-size:10.2px;line-height:17.5px;color:var(--body);height:70px;overflow:hidden;display:-webkit-box;-webkit-line-clamp:4;-webkit-box-orient:vertical}
.product-more{position:absolute;left:12px;top:111px;font-size:10.6px;line-height:14px;color:var(--green)}

.services{left:0;top:713px;width:864px;height:364px;background:var(--muted-bg)}
.services-title{top:728px}
.services-text{top:758px;padding:0 90px}
.service-box{top:810px;width:192px;height:242px;background:var(--white);text-align:center}
.service-head{height:45px;color:var(--white);font-size:19px;line-height:45px;letter-spacing:.4px}
.service-icon{display:block;margin:14px auto 0;width:56px;height:56px}
.service-text{font-size:10.2px;line-height:18px;color:var(--body);margin:8px 12px 0;height:72px;overflow:hidden;display:-webkit-box;-webkit-line-clamp:4;-webkit-box-orient:vertical}
.service-more{position:absolute;left:0;right:0;top:203px;font-size:10.6px;line-height:14px;display:flex;align-items:center;justify-content:center;gap:8px}
.dot-arrow{width:13px;height:13px;border-radius:50%;display:inline-flex;align-items:center;justify-content:center}

.site-footer{left:0;top:1103px;width:864px;height:97px;background:var(--green)}
.copyright{top:1135px;font-family:"Arimo",sans-serif;font-size:9.5px;color:var(--white)}
.social{left:374px;top:1158px;display:flex;gap:10px}
.social span{width:21px;height:21px;border-radius:50%;background:var(--white)}
</style>
</head>
<body>

<header class="abs site-header">
  <div class="abs brand">
    <span class="brand-mark"></span>
    <span class="brand-name">Brookfern Clinical Trials</span>
  </div>
  <nav class="abs main-nav">
    <a class="active" style="left:386px">HOME</a>
    <a style="left:458px">ABOUT US</a>
    <a style="left:549px">USER SUPPORT</a>
    <a style="left:664px">CONTACT US</a>
  </nav>
  <svg class="abs search" width="14" height="14" viewBox="0 0 14 14"><circle cx="5.5" cy="5.5" r="4" fill="none" stroke="#111" stroke-width="2"/><line x1="8.5" y1="8.5" x2="13" y2="13" stroke="#111" stroke-width="2.4" stroke-linecap="round"/></svg>
</header>
<div class="abs top-rule"><span style="width:295px;background:var(--orange)"></span><span style="width:312px;background:var(--green)"></span><span style="width:257px;background:var(--blue)"></span></div>

<section class="abs hero" role="img" aria-label="Doctor in a white coat holding a tablet at a desk beside a keyboard"></section>
<div class="abs hero-arrow" style="left:87px"><svg width="10" height="14" viewBox="0 0 10 14"><path d="M8 1 2 7l6 6" fill="none" stroke="#fff" stroke-width="2.6"/></svg></div>
<div class="abs hero-arrow" style="left:759px"><svg width="10" height="14" viewBox="0 0 10 14"><path d="M2 1l6 6-6 6" fill="none" stroke="#fff" stroke-width="2.6"/></svg></div>
<div class="abs hero-dots"><span></span><span></span><span></span></div>

<h1 class="abs center welcome-title">WELCOME TO BROOKFERN CLINICAL TRIALS</h1>
<p class="abs center lead welcome-text">Meridian Labelworks, Inc. specializes in providing products and services to the pharmaceutical industry. We are focused on the needs of those individuals involved with Clinical Trial Materials. Our products and services are summarized below.</p>

<h2 class="abs center section-title software-title">SOFTWARE PRODUCTS / SERVICES</h2>
<p class="abs center lead software-text">In magna modus duo. Ne vix etiam ludus. His ad habemus singulis, detracto accusata recteque eum ne, est et abhorreant ullamcorper. Solum velit iracundia te vix, cum habeo democritum ad.Cum no alii nonumes singulis.</p>

<article class="abs product-card" style="left:95px">
  <div class="product-photo" role="img" aria-label="Row of labelled vials in a lab rack" style="background:linear-gradient(180deg,#3d3a2c,#8a8466 55%,#2c2a20)"></div>
  <div class="product-body">
    <h3 class="product-title">LABELPRO/LBL™</h3>
    <p class="product-text">LabelPro/LBL™ is the industry's leading clinical label system offering superior overall capability and flexibility system enables user</p>
    <p class="product-more">Read More...</p>
  </div>
</article>
<article class="abs product-card" style="left:442px">
  <div class="product-photo" role="img" aria-label="Magnifying glass over a hard disk on a blue data background" style="background:linear-gradient(135deg,#0d2f57,#4a86b8 50%,#0b2848)"></div>
  <div class="product-body">
    <h3 class="product-title">SOFTWARE VALIDATION</h3>
    <p class="product-text">Meridian Labelworks offers validation services for the FDA regulated industry. Our knowledge of industry practices and standards</p>
    <p class="product-more">Read More...</p>
  </div>
</article>

<section class="abs services"></section>
<h2 class="abs center section-title services-title">OUR SERVICES</h2>
<p class="abs center lead services-text">Aperiri placerat ad has, nonumy dolores verterem an duo, ea mea aliquid nusquam. Quo at omittam intellegam, no vis tempor aliquip scriptorem. Pri wisi voluptua apeirian in. Pro eu sonet prodesset.</p>

<article class="abs service-box" style="left:124px">
  <div class="service-head" style="background:var(--orange)">LABELSERV</div>
  <svg class="service-icon" viewBox="0 0 56 56" fill="var(--orange)">
    <circle cx="21" cy="34" r="11"/>
    <g transform="translate(21 34)"><rect x="-3" y="-16" width="6" height="32"/><rect x="-16" y="-3" width="32" height="6"/><rect x="-3" y="-16" width="6" height="32" transform="rotate(45)"/><rect x="-3" y="-16" width="6" height="32" transform="rotate(-45)"/></g>
    <circle cx="21" cy="34" r="4.5" fill="#fff"/>
    <circle cx="39" cy="16" r="7.5"/>
    <g transform="translate(39 16)"><rect x="-2" y="-11" width="4" height="22"/><rect x="-11" y="-2" width="22" height="4"/><rect x="-2" y="-11" width="4" height="22" transform="rotate(45)"/><rect x="-2" y="-11" width="4" height="22" transform="rotate(-45)"/></g>
    <circle cx="39" cy="16" r="3" fill="#fff"/>
  </svg>
  <p class="service-text">LabelServ™ is a contract clinical label generation service that provides you with ready to apply clinical labels</p>
  <p class="service-more" style="color:var(--orange)">READ MORE <span class="dot-arrow" style="background:var(--orange)"><svg width="7" height="7" viewBox="0 0 7 7"><path d="M1 3.5h5M3.5 1 6 3.5 3.5 6" stroke="#fff" stroke-width="1.3" fill="none"/></svg></span></p>
</article>

<article class="abs service-box" style="left:337px">
  <div class="service-head" style="background:var(--green)">LABELBOOK</div>
  <svg class="service-icon" viewBox="0 0 56 56" fill="none" stroke="var(--green)" stroke-width="3.4" stroke-linejoin="round">
    <path d="M28 15c-6-4-14-5-22-3v34c8-2 16-1 22 3c6-4 14-5 22-3V12c-8-2-16-1-22 3z"/>
    <path d="M28 15v34"/>
    <path d="M11 8v3M45 8v3"/>
  </svg>
  <p class="service-text">LabelBook™ labels are multi-page clinical labels used to address the needs of multi-language studies.</p>
  <p class="service-more" style="color:var(--green)">READ MORE <span class="dot-arrow" style="background:var(--green)"><svg width="7" height="7" viewBox="0 0 7 7"><path d="M1 3.5h5M3.5 1 6 3.5 3.5 6" stroke="#fff" stroke-width="1.3" fill="none"/></svg></span></p>
</article>

<article class="abs service-box" style="left:548px">
  <div class="service-head" style="background:var(--blue)">RANDOMIZATIONS</div>
  <svg class="service-icon" viewBox="0 0 56 56" fill="none" stroke="var(--blue)" stroke-width="3.4" stroke-linecap="round">
    <path d="M14 6h-3v14c0 8 5 13 11 13s11-5 11-13V6h-3"/>
    <path d="M22 33v8c0 6 5 10 11 10s11-4 11-10v-8"/>
    <circle cx="44" cy="29" r="4"/>
  </svg>
  <p class="service-text">Our systems can create randomization data for all types of CTM needs. Patient randomization, material randomization</p>
  <p class="service-more" style="color:var(--blue)">READ MORE <span class="dot-arrow" style="background:var(--blue)"><svg width="7" height="7" viewBox="0 0 7 7"><path d="M1 3.5h5M3.5 1 6 3.5 3.5 6" stroke="#fff" stroke-width="1.3" fill="none"/></svg></span></p>
</article>

<footer class="abs site-footer"></footer>
<p class="abs center copyright">copyright 2015 Brookfern clinical, All right Reserved.</p>
<div class="abs social"><span></span><span></span><span></span><span></span></div>

</body>
</html>
```